Life and business Coaching Business Card and Logo

A new design for new company. We coach people to get the best out of themselves in business, life, health , family, career, relationships.
we work in Professional, executive, business and corporate environment. We use art and the processes of making art to work with getting people to delve into and change their mind maps or the way they are currently thinking so that they can move forward towards their goals strategically.
Updates

Project Deadline Extended
Reason: I have been laid up in bed with back problems and have just been able to get back to view designs. several are quiet good and I have given feedback today. I also want to take my project off refundable status as I will choose a design from this brief. regards Marisol

Target Market(s)

Professional artistic and bold energetic individuals

Industry/Entity Type

Health

Contact Information for Business Card

Vel5Mentoring, Marisol Drayke, Shaping Days Boldly,
Mob:0419586740, Ph: +61 8 95820647,
Professional, Executive, Business and Corporate Coach

Requirements
Must have
• a logo that can be used on all promotional and stationary material.
Should contain a person and be bold/colourful, simple and artistic.
Nice to have
• Room to place qualifications of Business

```html
<!DOCTYPE html>
<html lang="en">
<head>
<meta charset="utf-8">
<title>Vel5Mentoring – Business Card</title>
<link rel="stylesheet" href="https://fonts.googleapis.com/css2?family=Arimo:wght@400&display=swap">
<style>
  :root {
    --pink-light: #e69bb6;
    --pink-mid: #e2629b;
    --pink-deep: #dc167b;
    --lime: #e4e829;
    --white: #ffffff;
    --shadow: rgba(120, 20, 70, 0.35);
  }
  html, body {
    margin: 0;
    padding: 0;
    overflow: hidden;
  }
  body {
    width: 1200px;
    height: 675px;
  }
  .card {
    position: relative;
    width: 1200px;
    height: 675px;
    overflow: hidden;
    background: radial-gradient(circle at 444px 374px, var(--pink-light) 0%, var(--pink-mid) 50%, var(--pink-deep) 100%);
    font-family: "Arimo", Arial, sans-serif;
  }
  .brand {
    position: absolute;
    left: 540px;
    top: 200px;
    width: 560px;
  }
  .brand-name {
    margin: 0;
    color: var(--white);
    font-weight: 400;
    font-size: 80px;
    line-height: 1;
    letter-spacing: 1px;
    text-align: right;
  }
  .brand-tagline {
    margin: 18px 0 0;
    color: var(--lime);
    font-size: 19px;
    letter-spacing: 0.5px;
    word-spacing: 4px;
    text-align: right;
    white-space: nowrap;
  }
  .contact {
    position: absolute;
    left: 75px;
    top: 446px;
    color: var(--white);
    font-size: 29px;
    line-height: 37px;
    text-shadow: 1px 1px 2px var(--shadow);
    margin: 0;
  }
  .contact span {
    display: block;
  }
</style>
</head>
<body>
  <main class="card">
    <header class="brand">
      <h1 class="brand-name">Vel5Mentoring</h1>
      <p class="brand-tagline">PROFESSIONALS &nbsp;LEADING YOU TO SUCESS</p>
    </header>
    <address class="contact" style="font-style: normal;">
      <span class="contact-name">Marisol Drayke,</span>
      <span class="contact-role">Professional, Executive</span>
      <span class="contact-role">Business and Corporate Coach</span>
      <span class="contact-phone">Mob:0419586740, Ph: +61 8 95820647</span>
    </address>
  </main>
</body>
</html>
```